GLOR Duet Summit Poster

We are a cellular therapy (bone marrow transplants, etc) accreditation foundation who needs a poster design for a small workshop that we are going to host within a large workshop. The workshop will 1) Educate doctors who inspect program trying to get accredited. 2) Educate programs on how to become accredited.

It will be printed and mounted on foam board for display at the GLOR booth in exhibition halls. Dimensions should be 11 x 17 inches.

Our website is www.glorsite-example.org. The design does not have to have the same theme/colors as our website.

The poster should have written:

Cellular Therapy Inspection and Accreditation Workshop
February 10th, 2015
QRV Duet Summit
San Diego, CA

The statement below should be in small, subtle text to allow room for the other information. All returns, italics, and trademark symbols must be used exactly as included below:

The Halbrook Institute of Health Sciences, Office for Ongoing Learning is accredited by the Certification Board for Ongoing Clinical Learning to provide continuing medical education for physicians.

The Halbrook Institute of Health Sciences, Office for Ongoing Learning designates this live activity for a maximum of 7.5 OLB KTV Tier 1 Point(s)™. Physicians should claim only credit commensurate with the extent of their participation in the activity.

It should also have our logo on it (I have attached 2, use the one that has the best resolution)

Let me know if there are any questions!

```html
<!DOCTYPE html>
<html lang="en">
<head>
<meta charset="utf-8">
<title>GLOR Duet Summit Poster</title>
<link rel="stylesheet" href="https://fonts.googleapis.com/css2?family=Baumans&family=Arvo:wght@700&family=Arimo:wght@400;700&display=swap">
<style>
  :root {
    --frame-red: #a5161f;
    --brand-red: #e01d2a;
    --deep-red: #8c1118;
    --header-grey: #e3e3e3;
    --paper: #ffffff;
    --backdrop: #efefef;
    --sunset-top: #b8660f;
    --sunset-mid: #f0a21e;
    --sunset-low: #7a3a06;
    --label-bg: rgba(70, 70, 70, 0.55);
    --label-text: #ececec;
  }
  * { box-sizing: border-box; margin: 0; padding: 0; }
  html, body { width: 1000px; height: 1200px; overflow: hidden; }
  body { background: var(--backdrop); position: relative; }

  .poster {
    position: absolute; left: 132px; top: 33px;
    width: 735px; height: 1134px;
    background: var(--frame-red);
  }
  .poster__sheet {
    position: absolute; left: 15px; top: 14px; right: 15px; bottom: 15px;
    background: var(--paper);
  }
  .masthead {
    position: absolute; left: 15px; right: 15px; top: 28px; height: 157px;
    background: var(--header-grey);
    display: flex; align-items: center; justify-content: center;
  }
  .masthead__name {
    font-family: "Baumans", sans-serif; font-size: 92px; color: var(--brand-red);
    letter-spacing: 2px; line-height: 1;
  }
  .title {
    position: absolute; left: 15px; right: 15px; top: 190px; height: 112px;
    display: flex; flex-direction: column; align-items: center; justify-content: center;
    font-family: "Baumans", sans-serif; font-size: 36px; line-height: 1.36;
    color: var(--brand-red); text-align: center;
  }
  .photo-band {
    position: absolute; left: 0; right: 0; top: 302px; height: 566px;
    background: var(--frame-red);
  }
  .photo {
    position: absolute; left: 15px; right: 15px; top: 311px; height: 549px;
    background: linear-gradient(180deg, var(--sunset-top) 0%, var(--sunset-mid) 42%, #f6b431 50%, #c56a0c 62%, var(--sunset-low) 100%);
  }
  .photo__label {
    position: absolute; right: 0; bottom: 27px; width: 297px; height: 70px;
    background: var(--label-bg);
    display: flex; align-items: center; justify-content: center;
    font-family: "Baumans", sans-serif; font-size: 34px; color: var(--label-text);
  }
  .accreditation {
    position: absolute; left: 15px; right: 15px; top: 916px; height: 42px;
    background: var(--frame-red);
    display: flex; align-items: center; justify-content: center;
    padding: 0 14px;
    font-family: "Arimo", sans-serif; font-weight: 700; font-size: 11.5px; line-height: 1.3;
    color: var(--paper); text-align: center;
  }
  .designation {
    position: absolute; left: 15px; right: 15px; top: 962px; height: 60px;
    display: flex; align-items: center; justify-content: center;
    padding: 0 12px;
    font-family: "Arimo", sans-serif; font-size: 11.5px; line-height: 1.3;
    color: var(--deep-red); text-align: center;
  }
  .event-band {
    position: absolute; left: 15px; right: 15px; top: 1030px; height: 64px;
    background: linear-gradient(90deg, #ffffff 0%, var(--frame-red) 22%, var(--frame-red) 68%, #ffffff 100%);
    display: flex; flex-direction: column; align-items: center; justify-content: center;
    font-family: "Arvo", serif; font-weight: 700; font-size: 22px; line-height: 1.25;
    color: var(--paper); letter-spacing: 0.5px;
  }
</style>
</head>
<body>
  <main class="poster">
    <div class="poster__sheet"></div>

    <header class="masthead">
      <span class="masthead__name">GLOR</span>
    </header>

    <h1 class="title">
      <span>Cellular Therapy Inspection and</span>
      <span>Accreditation Workshop</span>
    </h1>

    <div class="photo-band"></div>
    <div class="photo" role="img" aria-label="Photograph of a long bridge on pillars silhouetted against an orange sunset over San Diego bay, the sun reflected on the water">
      <div class="photo__label">San Diego</div>
    </div>

    <p class="accreditation">The Halbrook Institute of Health Sciences, Office for Ongoing Learning is accredited by the Certification Board for Ongoing Clinical Learning to provide continuing medical education for physicians.</p>

    <p class="designation">The Halbrook Institute of Health Sciences, Office for Ongoing Learning designates this live activity for a maximum of 7.5 OLB KTV Tier 1 Point(s)™. Physicians should claim only credit commensurate with the extent of their participation in the activity.</p>

    <div class="event-band">
      <span>February 10th, 2015</span>
      <span>QRV Duet Summit San Diego, CA</span>
    </div>
  </main>
</body>
</html>
```